Crash Reapirer business card design

We are a crash repair business based in a small country town in South Australia with our own spray booth. We do all types of repairs for both insurance companies and private jobs. We also replace broken windscreens.
We usually have the KVL logo on our cards because we are KVL approved repairers.
We would also like the JPO (Vehicle Guild Federation)logo because we are a member for them also.
If the card could incorporate black, grey, white and silver colours that would be excellent.
We do not have our own logo if 1 could be created that would be great.

Industry/Entity Type

Insurance

Contact Information for Business Card

Dorvick Crash Repairs
47 Tulloch Ave, Renmark SA 5341
Ph 08 85213077 Fax 08 85213358
Kent 0412658341
Email - dorcrash@fernmail.com

We do private & insurance work, windscreen replacements on all makes & models of cars

```html
<!DOCTYPE html>
<html lang="en">
<head>
<meta charset="utf-8">
<title>Dorvick Crash Repairs – Business Card</title>
<link href="https://fonts.googleapis.com/css2?family=Michroma&family=Arimo:wght@400;700&display=swap" rel="stylesheet">
<style>
  :root {
    --page-bg: #d9d9d9;
    --card-black: #050608;
    --card-deep: #0d1418;
    --glow-soft: #1c3340;
    --text-white: #ffffff;
    --text-steel: #8fa3b0;
    --badge-blue: #5d79b8;
    --badge-yellow: #f2e200;
    --badge-frame: #ffffff;
  }
  * { box-sizing: border-box; margin: 0; padding: 0; }
  html, body {
    width: 1200px; height: 900px; overflow: hidden;
    background: var(--page-bg);
  }
  .business-card {
    position: absolute; left: 75px; top: 150px;
    width: 1050px; height: 600px;
    background: var(--card-black);
    overflow: hidden;
    box-shadow: 0 18px 40px rgba(0,0,0,.35);
  }
  .hero-car {
    position: absolute; left: 180px; top: 60px;
    width: 700px; height: 470px;
    background:
      radial-gradient(ellipse 45% 12% at 28% 52%, rgba(160,210,240,.55), transparent 70%),
      radial-gradient(ellipse 60% 45% at 50% 45%, var(--glow-soft), transparent 75%),
      radial-gradient(ellipse 80% 70% at 50% 75%, var(--card-deep), transparent 80%);
  }
  .address {
    position: absolute; top: 28px; right: 40px;
    font-family: "Michroma", sans-serif;
    font-size: 14px; letter-spacing: 4px;
    color: var(--text-white);
  }
  .brand-name {
    position: absolute; left: 240px; top: 205px;
    font-family: "Michroma", sans-serif;
    font-weight: 400;
    color: var(--text-white);
    text-transform: uppercase;
    line-height: 1;
  }
  .brand-name .brand-main { display: block; font-size: 66px; letter-spacing: 4px; }
  .brand-name .brand-sub { display: block; font-size: 30px; letter-spacing: 9px; margin: 6px 0 0 140px; }
  .contact {
    position: absolute; left: 130px; top: 355px;
    font-family: "Arimo", sans-serif;
    font-size: 25px; color: var(--text-white);
    text-align: right; line-height: 1.15;
  }
  .contact b { font-weight: 700; }
  .contact .email-line { display: block; margin-right: 100px; }
  .services {
    position: absolute; left: 50px; bottom: 46px;
    width: 680px;
    font-family: "Michroma", sans-serif;
    font-size: 12px; letter-spacing: 2.5px; line-height: 1.45;
    white-space: nowrap;
    color: var(--text-steel); text-transform: uppercase;
  }
  .badges { position: absolute; right: 40px; bottom: 40px; display: flex; gap: 10px; }
  .badge { width: 115px; height: 115px; }
  .badge-guild { background: var(--badge-blue); border: 3px solid var(--badge-frame); }
  .badge-approved { background: var(--badge-yellow); border: 6px solid var(--badge-frame); }
</style>
</head>
<body>
  <section class="business-card">
    <div class="hero-car" role="img" aria-label="Dark silhouette of a sports car with headlight glow"></div>
    <p class="address">47 Tulloch Ave, Renmark SA 5341</p>
    <h1 class="brand-name"><span class="brand-main">Dorvick</span><span class="brand-sub">Crash Repairs</span></h1>
    <p class="contact">
      phone: 08 85213077 / fax: 08 85213358 / <b>Kent</b>: 0412658341<br>
      <span class="email-line">email: dorcrash@fernmail.com</span>
    </p>
    <p class="services">We do private &amp; insurance work, windscreen<br>replacements on all makes &amp; models of cars</p>
    <div class="badges">
      <div class="badge badge-guild" role="img" aria-label="JPO Vehicle Guild Federation membership badge"></div>
      <div class="badge badge-approved" role="img" aria-label="KVL approved repairer badge"></div>
    </div>
  </section>
</body>
</html>
```